The Harborline LLC Asset Classes

I'm looking for for two designs here to go into powerpoint and potentially as a standalone PDF. My company does wealth management.
Graphic Image #1
I break down the investment world into 4 broad categories
-Preservation
-Capital Markets
-Real Estate
-Alternatives
In each broad category, there are subcategories:
Preservation: cash, checking/savings accounts, money market accounts, CD's, and fixed annuities.
Capital Markets: Publicly traded stocks and bonds
Real Estate: single-family residence, retail, industrial, multifamily, and office
Alternatives: private equity, private credit, cryptocurrency, asset-backed loans, tax liens, oil & gas, litigation finance, and royalties
Graphic 2: Please see the bottom f page 1 of the Tidewater Slides PDF.
Just like in graphic one, you have 4 categories of the Capital Markets and their respective subcategories
Category 1: Domestic Stocks: Subcategories are Large, mid, and small size companies
Category 2: International Stocks: Subcategories are Large, Mid/Small and by region - Developed and Emerging
Category 3: Fixed Income: You have subcategories like corporate, municipal, government, domestic, international
Category 4: Alternatives: The subcategories are metals and real estate
---------------------
I'm looking to create a graphic (either pie chart, or a circle broken into parts or some other clever way to illustrate this) to clearly illustrate both of these universes in a clean, professional, slick manner.
Target Market(s)
Investors
Colors
Designer to choose colors to be used in the design.
Requirements
Must have
- Clean
- professional
- Easy to read
- Creative
- Visually appealling
Nice to have
- I have attached my logo and some marketing materials so you can get a feel of what I am doing. Maybe you can clean this up too!

```html
<!DOCTYPE html>
<html lang="en">
<head>
<meta charset="utf-8">
<title>The Harborline LLC – Asset Classes</title>
<link rel="stylesheet" href="https://fonts.googleapis.com/css2?family=Lora:wght@600;700&family=Lato:wght@400;700&display=swap">
<style>
  :root{
    --backdrop:#6d6d6d;
    --paper:#ffffff;
    --navy:#1f5a8e;
    --orange:#e8902a;
    --green:#2b8a3e;
    --deep-teal:#12506b;
    --fixed-teal:#0c4f66;
    --light-teal:#3aaabf;
    --mid-teal:#2389a6;
    --slate:#9a9a9a;
    --ink:#2a2a2a;
    --wave-top:#1b5f86;
    --wave-bottom:#3fb0c4;
  }
  html,body{margin:0;padding:0;width:1200px;height:1200px;overflow:hidden;background:var(--backdrop);}
  .canvas{position:relative;width:1200px;height:1200px;}
  .slide{position:absolute;left:148px;width:904px;height:510px;background:var(--paper);box-shadow:0 6px 18px rgba(0,0,0,.35);}
  .slide--investment{top:40px;}
  .slide--capital{top:600px;}
  .slide svg{display:block;width:904px;height:510px;}
  .title{font-family:"Lora",Georgia,serif;font-weight:700;font-size:54px;fill:var(--navy);}
  .brand{font-family:"Lora",Georgia,serif;font-weight:700;font-size:30px;fill:var(--navy);}
  .heading{font-family:"Lora",Georgia,serif;font-weight:600;font-size:19px;}
  .item{font-family:"Lato",Arial,sans-serif;font-size:13.5px;fill:var(--ink);}
  .ring-label{font-family:"Lato",Arial,sans-serif;font-weight:700;font-size:19px;fill:#fff;letter-spacing:1.5px;}
  .ring-label--long{font-size:15px;letter-spacing:0.5px;}
  .page-no{font-family:"Lato",Arial,sans-serif;font-weight:700;font-size:12px;fill:#fff;}
  .icon{fill:none;stroke:#fff;stroke-width:2.5;stroke-linecap:round;stroke-linejoin:round;}
</style>
</head>
<body>
<div class="canvas">

  <section class="slide slide--investment" aria-label="Investment asset classes">
    <svg viewBox="0 0 1130 637" xmlns="http://www.w3.org/2000/svg">
      <defs>
        <linearGradient id="wave-a" x1="0" y1="0" x2="0" y2="1">
          <stop offset="0" stop-color="var(--wave-top)"/>
          <stop offset="1" stop-color="var(--wave-bottom)"/>
        </linearGradient>
        <path id="inv-pres-arc" d="M497 215 A66 66 0 0 1 629 215"/>
        <path id="inv-cap-arc" d="M460 388 A66 66 0 0 1 460 256"/>
        <path id="inv-re-arc" d="M671 256 A66 66 0 0 1 671 388"/>
        <path id="inv-alt-arc" d="M481 425 A83 83 0 0 0 647 425"/>
      </defs>

      <text class="title" x="38" y="72">Investment</text>
      <path d="M40 92 Q180 78 326 84" stroke="var(--orange)" stroke-width="4" fill="none" stroke-linecap="round"/>

      <g class="brand-lockup">
        <circle cx="790" cy="86" r="20" fill="var(--orange)"/>
        <text class="brand" x="820" y="97">The Harborline LLC</text>
      </g>

      <g stroke-width="1.2">
        <line x1="161" y1="183" x2="480" y2="183" stroke="var(--green)"/>
        <line x1="157" y1="340" x2="375" y2="340" stroke="var(--deep-teal)"/>
        <line x1="760" y1="295" x2="935" y2="295" stroke="var(--orange)"/>
        <line x1="660" y1="442" x2="953" y2="442" stroke="var(--slate)"/>
      </g>

      <g class="ring ring--capital">
        <circle cx="460" cy="322" r="97" fill="var(--deep-teal)"/>
        <circle cx="460" cy="322" r="47" fill="none" stroke="#fff" stroke-width="3"/>
        <g class="icon"><path d="M440 340 V320 M452 340 V310 M464 340 V300 M476 340 V292 M436 342 H482 M442 304 L472 286 M464 286 H472 V294"/></g>
        <text class="ring-label"><textPath href="#inv-cap-arc" startOffset="50%" text-anchor="middle">CAPITAL MARKETS</textPath></text>
      </g>
      <g class="ring ring--real-estate">
        <circle cx="671" cy="322" r="97" fill="var(--orange)"/>
        <circle cx="671" cy="322" r="47" fill="none" stroke="#fff" stroke-width="3"/>
        <g class="icon"><path d="M649 322 L671 302 L693 322 M655 317 V342 H687 V317 M666 342 V328 H676 V342"/></g>
        <text class="ring-label"><textPath href="#inv-re-arc" startOffset="50%" text-anchor="middle">REAL ESTATE</textPath></text>
      </g>
      <g class="ring ring--preservation">
        <circle cx="563" cy="215" r="97" fill="var(--green)"/>
        <circle cx="563" cy="215" r="47" fill="none" stroke="#fff" stroke-width="3"/>
        <g class="icon"><circle cx="563" cy="212" r="17"/><path d="M569 205 Q563 200 557 205 Q555 211 563 212 Q571 213 569 219 Q563 224 557 219 M563 198 V226"/></g>
        <text class="ring-label"><textPath href="#inv-pres-arc" startOffset="50%" text-anchor="middle">PRESERVATION</textPath></text>
      </g>
      <g class="ring ring--alternatives">
        <circle cx="563" cy="425" r="97" fill="var(--slate)"/>
        <circle cx="563" cy="425" r="47" fill="none" stroke="#fff" stroke-width="3"/>
        <g class="icon"><path d="M543 412 H583 M543 412 l6 -5 M543 412 l6 5 M583 412 l-6 -5 M583 412 l-6 5 M558 445 V424 Q563 418 568 424 V445"/></g>
        <text class="ring-label"><textPath href="#inv-alt-arc" startOffset="50%" text-anchor="middle">ALTERNATIVES</textPath></text>
      </g>
      <g class="hub">
        <circle cx="563" cy="322" r="42" fill="#fff" stroke="var(--deep-teal)" stroke-width="4"/>
        <circle cx="563" cy="322" r="22" fill="var(--mid-teal)"/>
      </g>

      <g class="list list--preservation">
        <text class="heading" x="161" y="178" fill="var(--green)">PRESERVATION</text>
        <g fill="var(--green)"><circle cx="164" cy="194" r="3"/><circle cx="164" cy="211" r="3"/><circle cx="164" cy="228" r="3"/><circle cx="164" cy="245" r="3"/><circle cx="164" cy="262" r="3"/></g>
        <text class="item" x="174" y="199">Cash</text>
        <text class="item" x="174" y="216">Checking/savings accounts</text>
        <text class="item" x="174" y="233">Money market accounts</text>
        <text class="item" x="174" y="250">CD's</text>
        <text class="item" x="174" y="267">Fixed annuities</text>
      </g>
      <g class="list list--capital">
        <text class="heading" x="157" y="335" fill="var(--deep-teal)">CAPITAL MARKETS</text>
        <g fill="var(--deep-teal)"><circle cx="161" cy="352" r="3"/><circle cx="161" cy="369" r="3"/></g>
        <text class="item" x="172" y="357">Publicly traded stocks</text>
        <text class="item" x="172" y="374">Bonds</text>
      </g>
      <g class="list list--real-estate">
        <text class="heading" x="805" y="290" fill="var(--orange)">REAL ESTATE</text>
        <g fill="var(--orange)"><circle cx="809" cy="306" r="3"/><circle cx="809" cy="323" r="3"/><circle cx="809" cy="340" r="3"/><circle cx="809" cy="357" r="3"/><circle cx="809" cy="374" r="3"/></g>
        <text class="item" x="819" y="311">Single-family Residence</text>
        <text class="item" x="819" y="328">Retail</text>
        <text class="item" x="819" y="345">Industrial</text>
        <text class="item" x="819" y="362">Multifamily</text>
        <text class="item" x="819" y="379">Office</text>
      </g>
      <g class="list list--alternatives">
        <text class="heading" x="803" y="437" fill="var(--slate)">ALTERNATIVES</text>
        <g fill="var(--slate)"><circle cx="809" cy="453" r="3"/><circle cx="809" cy="470" r="3"/><circle cx="809" cy="487" r="3"/><circle cx="809" cy="504" r="3"/><circle cx="809" cy="521" r="3"/><circle cx="809" cy="538" r="3"/><circle cx="809" cy="555" r="3"/><circle cx="809" cy="572" r="3"/></g>
        <text class="item" x="819" y="458">Private Equity</text>
        <text class="item" x="819" y="475">Private Credit</text>
        <text class="item" x="819" y="492">Cryptocurrency,</text>
        <text class="item" x="819" y="509">Asset-backed Loans</text>
        <text class="item" x="819" y="526">Tax Liens</text>
        <text class="item" x="819" y="543">Oil &amp; Gas</text>
        <text class="item" x="819" y="560">Litigation Finance</text>
        <text class="item" x="819" y="577">Royalties</text>
      </g>

      <path class="wave" d="M0 568 C250 545 480 552 700 578 C880 598 1020 592 1130 570 L1130 637 L0 637 Z" fill="url(#wave-a)"/>
      <circle cx="1052" cy="597" r="20" fill="var(--orange)" stroke="#fff" stroke-width="2"/>
      <text class="page-no" x="1052" y="601" text-anchor="middle">3</text>
    </svg>
  </section>

  <section class="slide slide--capital" aria-label="Capital markets asset classes">
    <svg viewBox="0 0 1130 637" xmlns="http://www.w3.org/2000/svg">
      <defs>
        <linearGradient id="wave-b" x1="0" y1="0" x2="0" y2="1">
          <stop offset="0" stop-color="var(--wave-top)"/>
          <stop offset="1" stop-color="var(--wave-bottom)"/>
        </linearGradient>
        <path id="cap-dom-arc" d="M498 221 A66 66 0 0 1 630 221"/>
        <path id="cap-fix-arc" d="M461 396 A66 66 0 0 1 461 264"/>
        <path id="cap-int-arc" d="M662.4 266.2 A64 64 0 1 1 662.4 393.8"/>
        <path id="cap-alt-arc" d="M481 436 A83 83 0 0 0 647 436"/>
      </defs>

      <text class="title" x="48" y="80">Capital Markets</text>
      <path d="M170 100 Q300 88 428 94" stroke="var(--orange)" stroke-width="4" fill="none" stroke-linecap="round"/>

      <g class="brand-lockup">
        <circle cx="790" cy="86" r="20" fill="var(--orange)"/>
        <text class="brand" x="820" y="97">The Harborline LLC</text>
      </g>

      <g stroke-width="1.2">
        <line x1="126" y1="214" x2="480" y2="214" stroke="var(--light-teal)"/>
        <line x1="123" y1="325" x2="375" y2="325" stroke="var(--fixed-teal)"/>
        <line x1="765" y1="333" x2="1055" y2="333" stroke="var(--orange)"/>
        <line x1="660" y1="452" x2="953" y2="452" stroke="var(--mid-teal)"/>
      </g>

      <g class="ring ring--fixed-income">
        <circle cx="461" cy="330" r="97" fill="var(--fixed-teal)"/>
        <circle cx="461" cy="330" r="47" fill="none" stroke="#fff" stroke-width="3"/>
        <g class="icon"><rect x="442" y="333" width="26" height="8" rx="3"/><rect x="442" y="323" width="26" height="8" rx="3"/><rect x="442" y="313" width="26" height="8" rx="3"/><circle cx="478" cy="312" r="9"/><path d="M438 350 H484"/></g>
        <text class="ring-label"><textPath href="#cap-fix-arc" startOffset="50%" text-anchor="middle">FIXED INCOME</textPath></text>
      </g>
      <g class="ring ring--international">
        <circle cx="668" cy="330" r="97" fill="var(--orange)"/>
        <circle cx="668" cy="330" r="47" fill="none" stroke="#fff" stroke-width="3"/>
        <g class="icon"><circle cx="668" cy="330" r="20"/><ellipse cx="668" cy="330" rx="9" ry="20"/><path d="M648 330 H688 M651 320 H685 M651 340 H685"/></g>
        <text class="ring-label ring-label--long"><textPath href="#cap-int-arc" startOffset="50%" text-anchor="middle">INTERNATIONAL STOCKS</textPath></text>
      </g>
      <g class="ring ring--domestic">
        <circle cx="564" cy="221" r="97" fill="var(--light-teal)"/>
        <circle cx="564" cy="221" r="47" fill="none" stroke="#fff" stroke-width="3"/>
        <g class="icon"><path d="M548 200 V226 M564 194 V222 M580 202 V230"/><rect x="545" y="206" width="6" height="12"/><rect x="561" y="200" width="6" height="14"/><rect x="577" y="208" width="6" height="14"/><path d="M542 240 L554 232 L566 238 L586 226"/></g>
        <text class="ring-label"><textPath href="#cap-dom-arc" startOffset="50%" text-anchor="middle">DOMESTIC STOCKS</textPath></text>
      </g>
      <g class="ring ring--alternatives">
        <circle cx="564" cy="436" r="97" fill="var(--mid-teal)"/>
        <circle cx="564" cy="436" r="47" fill="none" stroke="#fff" stroke-width="3"/>
        <g class="icon"><path d="M544 423 H584 M544 423 l6 -5 M544 423 l6 5 M584 423 l-6 -5 M584 423 l-6 5 M559 456 V435 Q564 429 569 435 V456"/></g>
        <text class="ring-label"><textPath href="#cap-alt-arc" startOffset="50%" text-anchor="middle">ALTERNATIVES</textPath></text>
      </g>
      <g class="hub">
        <circle cx="564" cy="330" r="42" fill="#fff" stroke="var(--fixed-teal)" stroke-width="4"/>
        <circle cx="564" cy="330" r="22" fill="var(--mid-teal)"/>
      </g>

      <g class="list list--domestic">
        <text class="heading" x="126" y="209" fill="var(--light-teal)">DOMESTIC STOCKS</text>
        <circle cx="130" cy="226" r="3" fill="var(--light-teal)"/>
        <text class="item" x="140" y="231">Large, mid, and small size companies</text>
      </g>
      <g class="list list--fixed-income">
        <text class="heading" x="123" y="320" fill="var(--fixed-teal)">FIXED INCOME</text>
        <g fill="var(--fixed-teal)"><circle cx="127" cy="336" r="3"/><circle cx="127" cy="353" r="3"/><circle cx="127" cy="370" r="3"/><circle cx="127" cy="387" r="3"/><circle cx="127" cy="404" r="3"/></g>
        <text class="item" x="138" y="341">Corporate</text>
        <text class="item" x="138" y="358">Municipal</text>
        <text class="item" x="138" y="375">Government</text>
        <text class="item" x="138" y="392">Domestic</text>
        <text class="item" x="138" y="409">International</text>
      </g>
      <g class="list list--international">
        <text class="heading" x="802" y="328" fill="var(--orange)">INTERNATIONAL STOCKS</text>
        <circle cx="807" cy="344" r="3" fill="var(--orange)"/>
        <text class="item" x="817" y="349">Large, Mid/Small and by region</text>
        <text class="item" x="817" y="366">Developed and Emerging</text>
      </g>
      <g class="list list--alternatives">
        <text class="heading" x="803" y="448" fill="var(--mid-teal)">ALTERNATIVES</text>
        <g fill="var(--mid-teal)"><circle cx="807" cy="464" r="3"/><circle cx="807" cy="481" r="3"/></g>
        <text class="item" x="817" y="469">Metals</text>
        <text class="item" x="817" y="486">Real Estate</text>
      </g>

      <path class="wave" d="M0 568 C250 545 480 552 700 578 C880 598 1020 592 1130 570 L1130 637 L0 637 Z" fill="url(#wave-b)"/>
      <circle cx="1054" cy="597" r="20" fill="var(--orange)" stroke="#fff" stroke-width="2"/>
      <text class="page-no" x="1054" y="601" text-anchor="middle">3</text>
    </svg>
  </section>

</div>
</body>
</html>
```